Business Cards for a law firm

Business cards for our law firm. Use our silhoette logo and OAK HARBOR - check our website (www.oakharbor-legal.com)

Contact Information for Business Card

our silhouette logo, OAK HARBOR, 800-555-0147, Dorian Kestrup, dorian@oakharbor-legal.com

Requirements
Must have
• our silhouette logo, OAK HARBOR, 800-555-0147, Dorian Kestrup, dorian@oakharbor-legal.com

```html
<!DOCTYPE html>
<html lang="en">
<head>
<meta charset="utf-8">
<title>Oak Harbor – Business Cards</title>
<link rel="stylesheet" href="https://fonts.googleapis.com/css2?family=Montserrat:wght@400;500;700&display=swap">
<style>
  :root {
    --navy: #1f2f7a;
    --navy-deep: #18256a;
    --navy-light: #3a4d9e;
    --ink: #4a4f63;
    --paper: #ffffff;
    --backdrop: #ecebe8;
    --rule: #b9bdd0;
  }
  * { margin: 0; padding: 0; box-sizing: border-box; }
  html, body { width: 1200px; height: 676px; overflow: hidden; }
  body {
    background: var(--backdrop);
    font-family: "Montserrat", Arial, sans-serif;
    display: flex; align-items: center; justify-content: center; gap: 60px;
  }
  .card {
    width: 500px; height: 286px; position: relative; overflow: hidden;
    box-shadow: 0 6px 18px rgba(0,0,0,.18);
  }
  /* Front */
  .card-front { background: var(--navy); }
  .card-front .pattern {
    position: absolute; inset: 0;
    background: linear-gradient(135deg, var(--navy-light) 0%, var(--navy) 50%, var(--navy-deep) 100%);
  }
  .card-front .brand {
    position: absolute; left: 50%; top: 50%; transform: translate(-50%, -50%);
    display: flex; align-items: center; gap: 12px;
    padding: 10px 16px; background: var(--navy);
  }
  .brand-dot { width: 30px; height: 30px; border-radius: 50%; background: var(--paper); flex: none; }
  .brand-name { color: var(--paper); font-weight: 500; font-size: 22px; letter-spacing: 2px; white-space: nowrap; }
  /* Back */
  .card-back { background: var(--paper); }
  .card-back .brand {
    position: absolute; left: 38px; top: 48px;
    display: flex; align-items: center; gap: 14px;
  }
  .card-back .brand-dot { width: 48px; height: 48px; background: var(--navy); }
  .card-back .brand-name { color: var(--navy); font-size: 36px; letter-spacing: 3px; }
  .person { position: absolute; left: 38px; top: 146px; text-align: right; width: 150px; }
  .person-name { color: var(--navy); font-weight: 700; font-size: 15px; white-space: nowrap; }
  .person-title { color: var(--ink); font-size: 11px; margin-top: 2px; }
  .divider { position: absolute; left: 204px; top: 146px; width: 1px; height: 64px; background: var(--rule); }
  .contacts { position: absolute; left: 216px; top: 146px; list-style: none; }
  .contacts li { display: flex; align-items: center; gap: 7px; font-size: 11.5px; color: var(--ink); height: 20px; }
  .contacts svg { width: 11px; height: 11px; fill: var(--navy); flex: none; }
  .address { position: absolute; left: 38px; top: 238px; font-size: 11px; color: var(--ink); }
</style>
</head>
<body>
  <section class="card card-front">
    <div class="pattern" role="img" aria-label="Repeating pattern of figure silhouettes in shades of blue"></div>
    <div class="brand">
      <span class="brand-dot"></span>
      <span class="brand-name">OAK HARBOR</span>
    </div>
  </section>

  <section class="card card-back">
    <div class="brand">
      <span class="brand-dot"></span>
      <span class="brand-name">OAK HARBOR</span>
    </div>
    <div class="person">
      <p class="person-name">Dorian Kestrup</p>
      <p class="person-title">Lawyer</p>
    </div>
    <span class="divider"></span>
    <ul class="contacts">
      <li><svg viewBox="0 0 24 24"><path d="M6.6 10.8a15.1 15.1 0 0 0 6.6 6.6l2.2-2.2a1 1 0 0 1 1-.25 11.4 11.4 0 0 0 3.6.57 1 1 0 0 1 1 1V20a1 1 0 0 1-1 1A17 17 0 0 1 3 4a1 1 0 0 1 1-1h3.5a1 1 0 0 1 1 1c0 1.25.2 2.45.57 3.57a1 1 0 0 1-.25 1z"/></svg>800-555-0147</li>
      <li><svg viewBox="0 0 24 24"><path d="M2 5h20v14H2zm2 2v.5l8 5 8-5V7l-8 5z"/></svg>dorian@oakharbor-legal.com</li>
      <li><svg viewBox="0 0 24 24"><path d="M12 2a10 10 0 1 0 0 20 10 10 0 0 0 0-20zm0 2c.9 1.2 1.6 2.6 2 4h-4c.4-1.4 1.1-2.8 2-4zM4.3 14a8 8 0 0 1 0-4h3.4a16 16 0 0 0 0 4zm1 2h3c.3 1.3.8 2.5 1.4 3.6A8 8 0 0 1 5.3 16zm3-8h-3a8 8 0 0 1 4.4-3.6C9.1 5.5 8.6 6.7 8.3 8zM12 20c-.9-1.2-1.6-2.6-2-4h4c-.4 1.4-1.1 2.8-2 4zm2.3-6H9.7a14 14 0 0 1 0-4h4.6a14 14 0 0 1 0 4zm.3 5.6c.6-1.1 1.1-2.3 1.4-3.6h3a8 8 0 0 1-4.4 3.6zM16.3 14a16 16 0 0 0 0-4h3.4a8 8 0 0 1 0 4zm-.3-6c-.3-1.3-.8-2.5-1.4-3.6A8 8 0 0 1 18.7 8z"/></svg>www.oakharbor-legal.com</li>
    </ul>
    <p class="address">415 Harbor View Rd, #12 Lakeport, OH 43017</p>
  </section>
</body>
</html>
```